Alcohol Marketing website

Home page and information page design, details as follows

CLIENT PURPOSE
Increase online visibility and create good contacts to increase business.

SERVICES
Drinks Marketing Consultancy
Brand Representation
Spirit Brand Sales & Marketing
Brand Development
Brand Distribution
Brand Launch & Introductions

COMPETITION
hazelpour.co.uk -
quintaloft.co.uk -

WEBSITE(S) CLIENT LIKES
Small competitors I admire:
http://www.hazelpour.co.uk/main.htm
http://www.quintaloft.com
http://www.morvatide.co.uk/spiritsliqueursbybrand.php
http://www.kelbrowhouse.com/page1.html
http://www.quorrifenwave.co.uk/index.asp

Nice page layout:
http://www.nkplume.com/
http://www.wzoharbour.com/
http://www.pelvit.com/index.cfm?do=pelvit.home

WEBSITE CLIENT DOES NOT LIKE
http://www.corvanhall.com/
http://www.amberlode-hall.com/
http://www.thesupperfold.co.uk/aboutUs.html
http://www.grainandkettle.com/
http://www.tessmarrow.co.uk/default.asp
http://www.pinnock-halden.co.uk/start.htm
http://www.rilby.co.uk/
http://www.vmkettles.com/default2.aspx
http://www.tumbril-vale.co.uk/mainpage.aspx

COMPANY LOGO
Customer has a company logo (Supplied)

COLOURS:
Blue
White

STRAPLINE:
No

WEBSITE THEME: Marketing

IMAGES THAT BEST REFLECT THE COMPANY:
Spirits / Drinks

HEADER IMAGE:
Spirits / Brands

PAGES:
home
strength& flavour
a little about us
our spirit marketing
big brand success
speak to us

USER JOURNEYS:
General Service > Land on website >Navigation > Info Pages > Contact Form
Questions > Land on website > Message Banners > Info Pages > Contact Form
Contact > Land on website > Clear Telephone / Email Banner > Contact Form

CALL TO ACTION BANNER:
If you need help making your drink the next big brand, speak to us today.

KEYWORDS THAT RELATE TO THE BUSINESS:
brand marketing
drinks marketing
spirits marketing
brand marketing strategy
alcoholic drinks marketing
Drinks Brand Development

LOCATION(S):
United Kingdom -
Worldwide -

Target Market(s)

Male & Female
30-60
Marketing Directors
Brand Developers
Export Directors
Brand Managers

Industry/Entity Type

Marketing

Number of Pages Required

2 pages

Requirements
Must have
• This design will be integrated into wordpress, I have attached a wireframe of what we need, this is NOT a strict guide but contains content that is essential, the wireframes shows the priority of statements and products. the images supplied need to sell the products and services.
The main banner will eventually be animated so this needs to be taken into account.
The cliemt has supplied images which will need to be used in the design , however if you feel you have better images in the same style then they can be used.
Nice to have
• animation included, Jquery
Should not have
• NO fully flash sites or designs, this site will be Search engine optimised and updateable

```html
<!DOCTYPE html>
<html lang="en">
<head>
<meta charset="utf-8">
<title>Grain &amp; Ember – Drinks Brand Marketing</title>
<link rel="stylesheet" href="https://fonts.googleapis.com/css2?family=Carlito:ital,wght@0,400;0,700;1,400;1,700&display=swap">
<style>
:root{
  --ink:#1d2b36;
  --ink-soft:#3c4852;
  --navy:#17324d;
  --white:#ffffff;
  --rule:#c9d0d5;
  --sky-top:#ffffff;
  --sky-mid:#cfe9f3;
  --sky-low:#3da5c9;
  --card-top:#2a8dba;
  --card-low:#8fcbe3;
  --social:#5aaed6;
}
*{margin:0;padding:0;box-sizing:border-box}
html,body{width:1200px;height:700px;overflow:hidden;background:var(--white)}
body{position:relative;font-family:"Carlito",sans-serif;color:var(--ink)}

.page{position:absolute;top:0;height:655px}
.page--home{left:18px;width:569px}
.page--about{left:610px;width:566px;height:652px}

.page__body{position:absolute;left:0;right:0;top:196px;bottom:0;
  background:linear-gradient(180deg,var(--sky-top) 0%,var(--sky-mid) 45%,#86c8e0 72%,var(--sky-low) 100%)}

.brand{position:absolute;top:66px;left:232px;font-weight:700;font-size:11px;letter-spacing:.3px;color:var(--ink);text-transform:uppercase}
.contact{position:absolute;top:87px;right:30px;text-align:right;font-size:9px;line-height:11px;color:var(--ink-soft)}
.social{position:absolute;top:94px;left:36px;display:flex;gap:4px}
.social span{width:20px;height:20px;border-radius:3px;background:var(--social)}

.banner{position:absolute;top:113px;left:0;right:0;height:51px;
  background:linear-gradient(90deg,#6c7785 0%,#a9b1ba 25%,#d7dadc 38%,#8a6d4d 55%,#b77427 68%,#d99b3d 80%,#f4efd6 93%,#ffffff 100%)}

.nav{position:absolute;top:164px;left:0;right:0;height:30px;display:flex;list-style:none;background:var(--white);border-bottom:1px solid var(--rule)}
.nav li{flex:1;text-align:center;font-size:10px;line-height:12px;color:var(--ink-soft);padding-top:2px;border-right:1px solid var(--rule)}
.nav li:last-child{border-right:0}

.photo{position:absolute}
.photo--cocktail{left:14px;top:213px;width:271px;height:254px;
  background:radial-gradient(circle at 60% 40%,#6b4a2e 0%,#2c1e16 45%,#12161f 100%)}
.photo--glasses{left:408px;top:253px;width:145px;height:92px;
  background:linear-gradient(135deg,#3a2a22,#c45c3a 55%,#e9b66b)}
.photo--bottles{left:408px;top:352px;width:145px;height:92px;
  background:linear-gradient(180deg,#1d2024,#8a6f4c 55%,#e7dcc4)}

.quote{position:absolute;right:12px;top:277px;text-align:right}
.quote__text{font-weight:700;font-size:31px;line-height:31px;letter-spacing:-1.4px;color:#141414}
.quote__cite{display:block;margin-top:8px;font-style:italic;font-size:10px;line-height:13px;letter-spacing:-.3px;color:var(--ink)}

.title{position:absolute;left:12px;top:216px;font-style:italic;font-weight:400;font-size:26px;color:#141414}
.about-copy{position:absolute;left:12px;top:253px;width:388px;font-style:italic;font-size:7.4px;line-height:8.4px;color:var(--ink)}
.about-copy p+p{margin-top:8px}

.features{position:absolute;top:493px;left:14px;width:542px;display:flex;justify-content:space-between}
.feature{width:163px;height:104px;padding:8px 12px;
  background:linear-gradient(180deg,var(--card-top) 0%,#5db0d5 35%,var(--card-low) 100%)}
.feature h2{font-style:italic;font-weight:400;font-size:13px;line-height:13.5px;color:var(--navy)}
.feature p{margin-top:10px;font-style:italic;font-weight:700;font-size:6.4px;line-height:8.2px;white-space:nowrap;color:var(--navy)}
.feature a{display:block;margin-top:13px;font-style:italic;font-size:7px;color:var(--navy);text-decoration:none}

.footer{position:absolute;left:0;right:0;top:620px;text-align:center;font-size:7.4px;line-height:13px;color:var(--white)}
</style>
</head>
<body>

<section class="page page--home">
  <div class="page__body"></div>
  <div class="brand">Grain &amp; Ember</div>
  <div class="social"><span></span><span></span></div>
  <div class="contact">t: 020 7946 0321<br>e-mail: info@grainandember.com</div>
  <div class="banner" role="img" aria-label="Header photograph of spirit bottles and glass with bubbles"></div>
  <ul class="nav">
    <li>home<br>page</li><li>grain<br>&amp; ember</li><li>a little bit<br>about us</li><li>our spirit<br>marketing</li><li>big brand<br>succes</li><li>our<br>blog</li><li>speak<br>to us</li>
  </ul>
  <div class="photo photo--cocktail" role="img" aria-label="Photograph of a cocktail glass on a bar counter"></div>
  <blockquote class="quote">
    <div class="quote__text">“turning our small<br>time whisky into a<br>national brand”</div>
    <cite class="quote__cite">Daniel Hartley<br>Velmora</cite>
  </blockquote>
  <div class="features">
    <article class="feature"><h2>22 years experience<br>with big brands</h2><p>Lorem ipsum dolor sit amet, consectetur<br>adipiscing elit. Aenean nec sagittis arcu.<br>Vivamus pharetra sem dapibus justo<br>placerat commodo semper lorem sagittis.</p><a href="#">Read More</a></article>
    <article class="feature"><h2>Making your drink<br>the next big brand</h2><p>Lorem ipsum dolor sit amet, consectetur<br>adipiscing elit. Aenean nec sagittis arcu.<br>Vivamus pharetra sem dapibus justo<br>placerat commodo semper lorem sagittis.</p><a href="#">Read More</a></article>
    <article class="feature"><h2>350 outlets that<br>listen to what we say</h2><p>Lorem ipsum dolor sit amet, consectetur<br>adipiscing elit. Aenean nec sagittis arcu.<br>Vivamus pharetra sem dapibus justo<br>placerat commodo semper lorem sagittis.</p><a href="#">Read More</a></article>
  </div>
  <footer class="footer">brand marketing | brand marketing strategy | drinks marketing | spirits marketing | alcoholic drinks marketing | drinks brand development<br>© 1999-2010 Grain &amp; Ember | terms and conditions | privacy policy</footer>
</section>

<section class="page page--about">
  <div class="page__body"></div>
  <div class="brand">Grain &amp; Ember</div>
  <div class="social"><span></span><span></span></div>
  <div class="contact">t: 020 7946 0321<br>e-mail: info@grainandember.com</div>
  <div class="banner" role="img" aria-label="Header photograph of spirit bottles and glass with bubbles"></div>
  <ul class="nav">
    <li>home<br>page</li><li>grain<br>&amp; ember</li><li>a little bit<br>about us</li><li>our spirit<br>marketing</li><li>big brand<br>succes</li><li>our<br>blog</li><li>speak<br>to us</li>
  </ul>
  <h1 class="title">a little bit about us</h1>
  <div class="about-copy">
    <p>Lorem ipsum dolor sit amet, consectetur adipiscing elit. Integer vestibulum quam non enim dignissim viverra. Vestibulum ante ipsum primis in faucibus orci luctus et ultrices posuere cubilia Curae; Ut semper, ligula eu iaculis laoreet, sem lacus sagittis felis, tristique suscipit lectus justo non nisl. Ut porta vestibulum tristique. Maecenas ornare est arcu. Donec fringilla tellus vel tellus fermentum euismod. Pellentesque venenatis magna posuere neque convallis viverra. Mauris massa nibh, convallis hendrerit suscipit vitae, dictum vitae enim. Maecenas blandit urna ac velit accumsan tempor. Aliquam lobortis vulputate diam eu tincidunt. Sed tincidunt risus quis urna malesuada imperdiet vel quis tortor. Sed et ante justo, sit amet rhoncus felis. Suspendisse ut volutpat tellus. Nulla sed velit ut purus vestibulum mattis. Praesent lorem nisi, mollis bibendum feugiat tincidunt, venenatis eget odio.</p>
    <p>Proin nec felis non dui lacinia condimentum. Etiam ullamcorper turpis sed mi laoreet in viverra ante ultrices. Nam dapibus est at sem dictum lobortis. Vivamus quis metus velit. Suspendisse fermentum dui vel nisi malesuada fringilla. Maecenas mattis lacus eu augue lacinia vestibulum. Cras commodo accumsan enim ac auctor. Sed a lectus purus, sed interdum erat. Nunc tincidunt sapien velit. Fusce sit amet tempus tortor. Vestibulum magna velit, egestas vel venenatis a, dictum eget dolor. Praesent tincidunt sagittis magna non imperdiet.</p>
    <p>Nulla vitae purus purus. Curabitur sit amet justo erat. Sed eu dui id mauris semper elementum eget eget urna. Integer et nulla erat. Maecenas egestas est sed ipsum accumsan sit amet placerat mi elementum. Pellentesque tellus lectus, blandit sed commodo sit amet, rutrum vel nisi. Sed tempor leo non est tempor id pretium tortor condimentum. Maecenas eget purus metus. Maecenas pharetra, mi eu eleifend placerat, leo mi ultrices lorem, vel imperdiet dolor nisi nec dolor. Proin rutrum pulvinar diam, non rhoncus elit viverra sit amet. Sed fermentum pretium nisi eu molestie. Aliquam vitae suscipit erat. In hac habitasse platea dictumst. Vestibulum iaculis tristique varius. Aenean cursus, urna in hendrerit porta, nulla leo porta justo, ut imperdiet lectus enim at leo. Praesent blandit ante ut erat vulputate semper. Donec hendrerit sapien dapibus massa mollis semper. Aliquam mauris mi, fermentum a bibendum dignissim, interdum id turpis. Aenean malesuada pretium accumsan.</p>
  </div>
  <div class="photo photo--glasses" role="img" aria-label="Photograph of colourful cocktails in glasses"></div>
  <div class="photo photo--bottles" role="img" aria-label="Photograph of spirit bottles on a back bar"></div>
  <div class="features">
    <article class="feature"><h2>22 years experience<br>with big brands</h2><p>Lorem ipsum dolor sit amet, consectetur<br>adipiscing elit. Aenean nec sagittis arcu.<br>Vivamus pharetra sem dapibus justo<br>placerat commodo semper lorem sagittis.</p><a href="#">Read More</a></article>
    <article class="feature"><h2>Making your drink<br>the next big brand</h2><p>Lorem ipsum dolor sit amet, consectetur<br>adipiscing elit. Aenean nec sagittis arcu.<br>Vivamus pharetra sem dapibus justo<br>placerat commodo semper lorem sagittis.</p><a href="#">Read More</a></article>
    <article class="feature"><h2>350 outlets that<br>listen to what we say</h2><p>Lorem ipsum dolor sit amet, consectetur<br>adipiscing elit. Aenean nec sagittis arcu.<br>Vivamus pharetra sem dapibus justo<br>placerat commodo semper lorem sagittis.</p><a href="#">Read More</a></article>
  </div>
  <footer class="footer">brand marketing | brand marketing strategy | drinks marketing | spirits marketing | alcoholic drinks marketing | drinks brand development<br>© 1999-2010 Grain &amp; Ember | terms and conditions | privacy policy</footer>
</section>

</body>
</html>
```